Letterhead to Introduce a 'Sister' Company.

What I am needing is a design for a letter head to introduce our current customers base of (KT Alarm) customers to our new service, 'Kestrel Tide Solar Brokers'

```html
<!DOCTYPE html>
<html lang="en">
<head>
<meta charset="utf-8">
<title>KT Alarm – Letterhead</title>
<link href="https://fonts.googleapis.com/css2?family=Questrial&family=Montserrat:wght@700&display=swap" rel="stylesheet">
<style>
  :root {
    --canvas: #ffffff;
    --page: #ffffff;
    --page-edge: #d6d6d6;
    --ink: #2b2b2b;
    --brand-green: #5bb531;
    --brand-blue: #1b4f93;
    --accent-orange: #f2a51a;
    --sun-tint: #f3f3f3;
  }
  * { margin: 0; padding: 0; box-sizing: border-box; }
  html, body {
    width: 1200px;
    height: 1000px;
    overflow: hidden;
    background: var(--canvas);
  }
  .letterhead {
    position: absolute;
    left: 258px;
    top: 16px;
    width: 684px;
    height: 967px;
    background: var(--page);
    border: 1px solid var(--page-edge);
    overflow: hidden;
    font-family: "Questrial", "Century Gothic", sans-serif;
    color: var(--ink);
  }
  .sun-backdrop {
    position: absolute;
    left: 140px;
    top: 210px;
    width: 544px;
    height: 757px;
    background: radial-gradient(circle at 412px 414px,
      var(--sun-tint) 0, var(--sun-tint) 200px,
      rgba(243,243,243,0.6) 260px,
      rgba(243,243,243,0) 420px);
  }
  .sender-name {
    position: absolute;
    left: 52px;
    top: 74px;
    font-family: "Montserrat", sans-serif;
    font-weight: 700;
    font-size: 31px;
    letter-spacing: 0.5px;
    color: var(--brand-green);
  }
  .contact {
    position: absolute;
    right: 42px;
    top: 74px;
    text-align: right;
    font-size: 13px;
    line-height: 17px;
  }
  .contact .address { margin-top: 15px; }
  .footer-web {
    position: absolute;
    left: 48px;
    top: 882px;
    font-size: 14px;
    letter-spacing: 1.6px;
    color: var(--ink);
  }
  .footer-rule {
    position: absolute;
    left: 48px;
    top: 904px;
    width: 586px;
    height: 1.5px;
    background: var(--accent-orange);
  }
  .sister-brand {
    position: absolute;
    right: 50px;
    top: 850px;
    display: flex;
    align-items: center;
    gap: 8px;
  }
  .sister-brand .mark {
    width: 14px;
    height: 14px;
    border-radius: 50%;
    background: var(--accent-orange);
  }
  .sister-brand .name {
    font-family: "Montserrat", sans-serif;
    font-weight: 700;
    font-size: 13px;
    line-height: 15px;
    letter-spacing: 0.6px;
    color: var(--brand-blue);
    text-align: right;
    text-transform: uppercase;
  }
</style>
</head>
<body>
  <main class="letterhead">
    <div class="sun-backdrop" role="img" aria-label="Large faint grey sun with radiating rays as a watermark decoration"></div>

    <div class="sender-name">KT Alarm</div>

    <address class="contact" style="font-style: normal;">
      <div class="phone">0412 775 308</div>
      <div class="email">info@kestreltide.com</div>
      <div class="address">58 Harbour Rd., Coral Bay,<br>Any Town, US 204918</div>
    </address>

    <div class="sister-brand">
      <span class="mark"></span>
      <span class="name">Kestrel Tide<br>Solar Brokers</span>
    </div>

    <div class="footer-web">www.kestreltide.com</div>
    <div class="footer-rule"></div>
  </main>
</body>
</html>
```